Business Card Update, need to bring life to the card, two sided color

We need a new business card design, are moving and changing addresses and need a new look, we have the logos already attached but need a new style moving forward. Can incorporate the color of the logo (The Green) as well, maybe a solid back? We deal with safety products revolving around static electricity and safety lighting. Would like to keep same font in second logo as well.

Target Market(s)

Electrical Safety, Lighting

Contact Information for Business Card

Lars Whitcombe
Vice President
Office: 555-284-7316
Cell: 555-862-0457
lars@tkwhitcombe.com
www.tkwhitcombe.com
4700 West Cedar Boulevard
Suite #320
Roswell, GA 30412

Font styles to use
Serif
Sans Serif

Requirements
Must have
• Since 1918
Nice to have
• Could use the 100 Year Logo for back of card, would like the back of card to be the same green as logo.
Should not have
• No black cards please.

```html
<!DOCTYPE html>
<html lang="en">
<head>
<meta charset="utf-8">
<title>T.K. Whitcombe Business Card</title>
<link href="https://fonts.googleapis.com/css2?family=Arimo:wght@400;700&family=Open+Sans:wght@300;400;700&display=swap" rel="stylesheet">
<style>
  :root {
    --page: #e6e6e4;
    --green: #1f9a3e;
    --green-deep: #15692b;
    --forest: #123a22;
    --white: #ffffff;
    --mint: #7fd49a;
  }
  * { box-sizing: border-box; margin: 0; padding: 0; }
  html, body { width: 1200px; height: 1020px; overflow: hidden; }
  body {
    background: var(--page);
    display: flex;
    flex-direction: column;
    align-items: center;
    justify-content: center;
    gap: 60px;
    font-family: "Open Sans", sans-serif;
  }
  .card {
    position: relative;
    width: 620px;
    height: 354px;
    border-radius: 4px;
    box-shadow: 0 6px 18px rgba(0,0,0,0.25);
    overflow: hidden;
  }

  /* logo side: solid brand green */
  .card-logo { background: var(--green); }
  .logo-mark {
    position: absolute;
    left: 48px;
    top: 52px;
    width: 250px;
    height: 250px;
    border-radius: 50%;
    background: var(--green-deep);
  }
  .logo-brand {
    position: absolute;
    left: 326px;
    top: 136px;
    color: var(--white);
    font-family: "Arimo", sans-serif;
    font-weight: 700;
  }
  .logo-brand .brand-name { font-size: 27px; line-height: 1.15; }
  .logo-brand .brand-sub { font-size: 12px; line-height: 1.4; }
  .since {
    margin-top: 14px;
    font-family: "Arimo", sans-serif;
    font-weight: 400;
    font-size: 12px;
    letter-spacing: 3px;
    text-transform: uppercase;
    color: var(--white);
  }

  /* contact side: deep forest green */
  .card-contact { background: var(--forest); }
  .contact-brand {
    position: absolute;
    right: 36px;
    top: 40px;
    display: flex;
    align-items: center;
    gap: 10px;
    color: var(--green);
    font-family: "Arimo", sans-serif;
    font-weight: 700;
  }
  .contact-brand .dot {
    width: 46px; height: 46px; border-radius: 50%;
    background: var(--green);
  }
  .contact-brand .brand-name { font-size: 17px; line-height: 1.15; color: var(--mint); }
  .contact-brand .brand-sub { font-size: 9px; line-height: 1.4; color: var(--mint); }
  .person {
    position: absolute;
    left: 44px;
    top: 150px;
  }
  .person-name {
    color: var(--white);
    font-size: 22px;
    font-weight: 300;
    letter-spacing: 0.5px;
    line-height: 1.2;
  }
  .person-name strong { font-weight: 700; }
  .person-title {
    color: var(--mint);
    font-size: 11px;
    letter-spacing: 0.5px;
    margin-top: 2px;
  }
  .rule {
    width: 52px;
    height: 2px;
    background: var(--green);
    margin-top: 12px;
  }
  .contacts {
    position: absolute;
    left: 44px;
    bottom: 40px;
    list-style: none;
    color: var(--white);
    font-size: 13px;
    line-height: 1.6;
  }
  .contacts li { display: flex; align-items: center; gap: 8px; }
  .contacts svg { width: 12px; height: 12px; fill: var(--mint); flex: none; }
  .contacts .no-icon { padding-left: 20px; }
</style>
</head>
<body>
  <section class="card card-logo">
    <div class="logo-mark" role="img" aria-label="Company emblem area"></div>
    <div class="logo-brand">
      <div class="brand-name">T.K. Whitcombe</div>
      <div class="brand-sub">Manufacturing Company, Inc.</div>
      <div class="since">Since 1918</div>
    </div>
  </section>

  <section class="card card-contact">
    <div class="contact-brand">
      <div class="dot" aria-hidden="true"></div>
      <div>
        <div class="brand-name">T.K. Whitcombe</div>
        <div class="brand-sub">Manufacturing Company, Inc.</div>
      </div>
    </div>

    <div class="person">
      <div class="person-name">YOUR <strong>NAME</strong></div>
      <div class="person-title">JOB TITLE</div>
      <div class="rule"></div>
    </div>

    <ul class="contacts">
      <li>
        <svg viewBox="0 0 24 24" aria-hidden="true"><path d="M6.6 10.8a15 15 0 0 0 6.6 6.6l2.2-2.2a1 1 0 0 1 1-.25 11.4 11.4 0 0 0 3.6.57 1 1 0 0 1 1 1V20a1 1 0 0 1-1 1A17 17 0 0 1 3 4a1 1 0 0 1 1-1h3.5a1 1 0 0 1 1 1c0 1.25.2 2.45.57 3.57a1 1 0 0 1-.25 1z"/></svg>
        000 000 0000
      </li>
      <li>
        <svg viewBox="0 0 24 24" aria-hidden="true"><path d="M2 5h20v14H2z M4 7v.5l8 5 8-5V7l-8 5z" fill-rule="evenodd"/></svg>
        youremail@xyz.com
      </li>
      <li>
        <svg viewBox="0 0 24 24" aria-hidden="true"><circle cx="12" cy="12" r="10"/></svg>
        www.yourwebsite.com
      </li>
      <li class="no-icon">Street Address, City, ST Zip Code</li>
    </ul>
  </section>
</body>
</html>
```